Lantern Holdings Business Card

We are looking to design new business cards for our company. We have two office locations and would like to have both full addresses on the card. Each address needs two lines for the building name and street address and a line or two for the city, state and zip code. There should be a place for 2-3 phone numbers. The addresses and phone numbers are at the bottom of this description. We also need a place to put our company website and one email address. Our logo is attached.
We would like the card to be two sided. The back of the card should have a blue background with some part of our logo design on it. We would like the full logo on the front of the card as well. The front of the card should have a white background with the blue logo. We are open to listing our addresses on the front or the back of the card. The person who designed our logo gave us an excellent business card idea that we really liked. I have attached a picture of his business card idea so that we can build off of it.
Addresses:
The Marlow Exchange
2214 47th Street NW
Washington, DC 20419
Osprey Harbor Tower
815 Tamsin Boulevard #2207
Miami, FL 33987
Phone Numbers: (202) 555-0148
(202) 555-0193
Website: www.lanternholdings-example.com

```html
<!DOCTYPE html>
<html lang="en">
<head>
<meta charset="utf-8">
<title>Lantern Holdings Business Card</title>
<link rel="stylesheet" href="https://fonts.googleapis.com/css2?family=PT+Sans+Narrow:wght@400;700&display=swap">
<style>
  :root {
    --backdrop: #7f8083;
    --shadow: #4a4b4e;
    --card-white: #ffffff;
    --navy: #2b3078;
    --ink: #2e3185;
    --brand-blue: #0058ae;
    --rule: #6b6c9c;
    --accent-bar: #9c9dc9;
    --light: #ffffff;
  }
  * { margin: 0; padding: 0; box-sizing: border-box; }
  html, body { width: 983px; height: 1200px; overflow: hidden; }
  body {
    position: relative;
    background: var(--backdrop);
    font-family: "PT Sans Narrow", "Arial Narrow", sans-serif;
  }
  .card {
    position: absolute;
    left: 27px;
    width: 915px;
    height: 526px;
    box-shadow: 7px 7px 0 var(--shadow);
  }
  .card--front { top: 41px; background: var(--card-white); border: 2px solid #111; }
  .card--back { top: 617px; background: var(--navy); }

  /* Front */
  .brand-square {
    position: absolute; left: 133px; top: 184px;
    width: 132px; height: 132px;
    background: var(--ink);
    border-radius: 14px;
  }
  .brand-name {
    position: absolute; left: 279px; top: 172px;
    color: var(--ink);
    font-weight: 400;
    text-transform: uppercase;
    line-height: 1;
  }
  .brand-name__main { display: block; font-size: 112px; letter-spacing: 14px; }
  .brand-name__sub { display: block; font-size: 52px; letter-spacing: 24px; margin-top: 2px; padding-left: 12px; }
  .front-rule {
    position: absolute; left: 54px; top: 442px;
    width: 802px; height: 2px; background: var(--rule);
  }
  .contact-row {
    position: absolute; top: 464px; left: 0; right: 0;
    color: var(--ink); font-weight: 700; font-size: 21px; line-height: 28px;
  }
  .contact-row span { position: absolute; white-space: nowrap; }
  .contact-row .phone-1 { left: 129px; }
  .contact-row .divider { left: 292px; }
  .contact-row .phone-2 { left: 318px; }
  .contact-row .site { left: 537px; }

  /* Back */
  .back-mark {
    position: absolute; left: 73px; top: 93px;
    width: 361px; height: 364px;
    background: var(--brand-blue);
    border-radius: 34px;
  }
  .office { position: absolute; left: 521px; height: 82px; }
  .office--dc { top: 107px; }
  .office--miami { top: 227px; }
  .office__bar {
    position: absolute; left: 0; top: 0;
    width: 9px; height: 82px; background: var(--accent-bar);
  }
  .office address {
    position: absolute; left: 42px; top: -4px;
    font-style: normal; color: var(--light);
    font-size: 24px; line-height: 30px; white-space: nowrap;
  }
  .back-phones {
    position: absolute; left: 514px; top: 350px;
    color: var(--light); font-size: 38px; line-height: 50px;
  }
  .back-phones p { white-space: nowrap; }
</style>
</head>
<body>
  <section class="card card--front" aria-label="Card front">
    <div class="brand-square"></div>
    <h1 class="brand-name">
      <span class="brand-name__main">Lantern</span>
      <span class="brand-name__sub">Holdings</span>
    </h1>
    <div class="front-rule"></div>
    <p class="contact-row">
      <span class="phone-1">(202) 555 - 0148</span>
      <span class="divider">|</span>
      <span class="phone-2">(202) 555 - 0193</span>
      <span class="site">www.lanternholdings-example.com</span>
    </p>
  </section>

  <section class="card card--back" aria-label="Card back">
    <div class="back-mark"></div>
    <div class="office office--dc">
      <div class="office__bar"></div>
      <address>The Marlow Exchange<br>2214 47th Street NW<br>Washington, DC 20419</address>
    </div>
    <div class="office office--miami">
      <div class="office__bar"></div>
      <address>Osprey Harbor Tower<br>815 Tamsin Boulevard #2207<br>Miami, FL 33987</address>
    </div>
    <div class="back-phones">
      <p>(202) 555-0148</p>
      <p>(202) 555-0193</p>
    </div>
  </section>
</body>
</html>
```